Postcard Project

I need a postcard designed 6X9 in size printed full color
Will need in the end a high resolution print ready file with crop marks
See instructions in word doc

```html
<!DOCTYPE html>
<html lang="en">
<head>
<meta charset="utf-8">
<title>Drinkware Postcard</title>
<link href="https://fonts.googleapis.com/css2?family=Roboto:ital,wght@0,400;0,700;0,900;1,900&display=swap" rel="stylesheet">
<style>
  :root {
    --navy: #0d355a;
    --red: #ee3b24;
    --green: #b2d235;
    --white: #ffffff;
    --ink: #1a1a1a;
    --stamp: #e5e6e8;
  }
  html, body { margin: 0; padding: 0; }
  body {
    width: 921px; height: 1200px; overflow: hidden; position: relative;
    background: var(--white);
    font-family: "Roboto", Arial, sans-serif;
  }
  .card {
    position: absolute; left: 104px; width: 714px; height: 476px;
    background: var(--white); overflow: hidden;
    box-shadow: 0 6px 14px rgba(0,0,0,.25);
  }
  .card--front { top: 79px; }
  .card--back { top: 617px; }
  .card__shapes { position: absolute; left: 0; top: 0; }
  .abs { position: absolute; margin: 0; }

  /* front */
  .brand { left: 24px; top: 34px; width: 166px; text-align: center; color: var(--navy); font-weight: 700; font-size: 17px; letter-spacing: 1px; line-height: 1.15; }
  .brand__dot { display: inline-block; width: 8px; height: 8px; border-radius: 50%; background: var(--red); margin-right: 5px; vertical-align: middle; }
  .headline { left: 241px; top: 28px; color: var(--white); font-weight: 900; font-size: 25px; line-height: 30px; }
  .product { border-radius: 6px; }
  .caption { font-size: 10px; line-height: 12px; color: var(--ink); white-space: nowrap; }
  .caption--center { text-align: center; transform: translateX(-50%); }
  .hero-caption { left: 106px; top: 415px; transform: translateX(-50%); text-align: center; color: var(--white); font-size: 15px; line-height: 18px; white-space: nowrap; }
  .category { right: 24px; top: 388px; color: var(--red); font-weight: 900; font-size: 38px; line-height: 40px; }
  .promo-line { right: 24px; top: 441px; color: var(--white); font-size: 19px; line-height: 22px; }

  /* back */
  .pill { background: var(--red); color: var(--white); font-weight: 700; font-size: 17px; border-radius: 6px; height: 34px; line-height: 34px; text-align: center; }
  .code-label { color: var(--white); font-size: 13px; line-height: 16px; }
  .code-box { background: var(--white); border-radius: 6px; height: 34px; line-height: 34px; text-align: center; color: var(--red); font-weight: 900; font-style: italic; font-size: 21px; }
  .body-copy { color: var(--white); font-size: 13px; line-height: 16px; left: 25px; }
  .notice { left: 25px; top: 219px; width: 353px; height: 22px; line-height: 22px; border-radius: 11px; background: var(--red); color: var(--white); font-weight: 700; font-size: 12.5px; text-align: center; }
  .section-label { left: 25px; color: var(--white); font-size: 14px; line-height: 16px; }
  .stamp { left: 610px; top: 28px; width: 73px; height: 73px; background: var(--stamp); }
  .return-copy { right: 31px; top: 424px; text-align: right; font-size: 11px; line-height: 15px; color: var(--ink); }
</style>
</head>
<body>

<section class="card card--front">
  <svg class="card__shapes" width="714" height="476" viewBox="0 0 714 476">
    <polygon points="0,93 285,334 222,476 0,476" fill="var(--red)"/>
    <polygon points="0,101 255,329 189,476 0,476" fill="var(--navy)"/>
    <path d="M236,14 H714 V99 H236 A25,25 0 0 1 211,74 V39 A25,25 0 0 1 236,14 Z" fill="var(--red)"/>
    <polygon points="296,427 714,427 714,476 277,476" fill="var(--navy)"/>
    <g transform="translate(620,63)">
      <polygon fill="var(--green)" points="60,0 48.1,9.6 55.4,23 40.7,27.2 42.4,42.4 27.2,40.7 23,55.4 9.6,48.1 0,60 -9.6,48.1 -23,55.4 -27.2,40.7 -42.4,42.4 -40.7,27.2 -55.4,23 -48.1,9.6 -60,0 -48.1,-9.6 -55.4,-23 -40.7,-27.2 -42.4,-42.4 -27.2,-40.7 -23,-55.4 -9.6,-48.1 0,-60 9.6,-48.1 23,-55.4 27.2,-40.7 42.4,-42.4 40.7,-27.2 55.4,-23 48.1,-9.6"/>
      <g transform="rotate(-15)" fill="var(--navy)" font-family="Roboto, Arial, sans-serif" font-weight="900" text-anchor="middle">
        <text x="-4" y="-4" font-size="30">$50</text>
        <text x="6" y="26" font-size="30">off</text>
      </g>
    </g>
  </svg>

  <p class="abs brand"><span class="brand__dot"></span>LAKESHORE<br>PROMOTIONS</p>
  <h1 class="abs headline">ON YOUR DRINKWARE<br>ORDER OVER $500</h1>

  <div class="abs product" role="img" aria-label="White insulated tumbler with black lid and cork base" style="left:44px;top:106px;width:123px;height:290px;background:linear-gradient(#1a1a1a 0 14%, #f4f4f4 14% 84%, #8a4a30 84%);border-radius:14px 14px 40px 40px;"></div>
  <p class="abs hero-caption">DW-2210WH_A_FR_4186<br>Black</p>

  <p class="abs caption" style="left:216px;top:126px;">3417-52SL_C_SIDE<br>Black</p>
  <div class="abs product" role="img" aria-label="Silver twisted steel tumbler" style="left:216px;top:155px;width:53px;height:107px;background:linear-gradient(90deg,#c9ccd0,#f3f4f5,#b8bcc1);border-radius:6px 6px 14px 14px;"></div>

  <p class="abs caption" style="left:285px;top:164px;">DW-3308RBL_A__2614<br>White</p>
  <div class="abs product" role="img" aria-label="Blue plastic sport bottle" style="left:285px;top:196px;width:37px;height:110px;background:linear-gradient(90deg,#2f5bb8,#4a78d6,#2a50a6);border-radius:10px 10px 6px 6px;"></div>

  <p class="abs caption" style="left:341px;top:222px;">3418-27RD_C_SIDE<br>White</p>
  <div class="abs product" role="img" aria-label="Red steel water bottle with loop cap" style="left:341px;top:256px;width:31px;height:120px;background:linear-gradient(90deg,#9e2f2a,#c5433b,#8f2924);border-radius:12px 12px 6px 6px;"></div>

  <div class="abs product" role="img" aria-label="Red plastic stadium cup" style="left:483px;top:125px;width:59px;height:86px;background:linear-gradient(90deg,#b4161b,#dc2a2a,#a81217);border-radius:4px 4px 14px 14px;"></div>
  <p class="abs caption caption--center" style="left:512px;top:221px;">DW-4470RD_A_FR<br>Black</p>

  <div class="abs product" role="img" aria-label="White camp mug with clear lid" style="left:596px;top:126px;width:83px;height:78px;background:linear-gradient(90deg,#dcdcdc,#f5f5f5,#d0d0d0);"></div>
  <p class="abs caption caption--center" style="left:647px;top:218px;">3418-63WH_C_SIDE<br>Full Color</p>

  <div class="abs product" role="img" aria-label="Black ceramic mug" style="left:468px;top:256px;width:89px;height:78px;background:linear-gradient(90deg,#0e0e0e,#2b2b2b,#0a0a0a);border-radius:6px 6px 18px 18px;"></div>
  <p class="abs caption caption--center" style="left:512px;top:354px;">3421-18BK_C_FR_5032<br>White</p>

  <div class="abs product" role="img" aria-label="White mug with speckled clay base" style="left:611px;top:256px;width:72px;height:78px;background:linear-gradient(#f1f1ec 0 64%, #a39a6e 64%);border-radius:6px 6px 14px 14px;"></div>
  <p class="abs caption caption--center" style="left:647px;top:354px;">3421-45WH_C_FR_8817<br>Full</p>

  <h2 class="abs category">DRINKWARE</h2>
  <p class="abs promo-line">Promo Code DRINK Good till 9/30/25</p>
</section>

<section class="card card--back">
  <svg class="card__shapes" width="714" height="476" viewBox="0 0 714 476">
    <polygon points="0,0 464,0 389,298 0,298" fill="var(--navy)"/>
    <polygon points="0,367 330,367 320,406 0,406" fill="var(--navy)"/>
    <polygon points="464,0 474,0 372,476 343,476" fill="var(--red)"/>
    <g transform="translate(361,381)">
      <polygon fill="var(--green)" points="60,0 48.1,9.6 55.4,23 40.7,27.2 42.4,42.4 27.2,40.7 23,55.4 9.6,48.1 0,60 -9.6,48.1 -23,55.4 -27.2,40.7 -42.4,42.4 -40.7,27.2 -55.4,23 -48.1,9.6 -60,0 -48.1,-9.6 -55.4,-23 -40.7,-27.2 -42.4,-42.4 -27.2,-40.7 -23,-55.4 -9.6,-48.1 0,-60 9.6,-48.1 23,-55.4 27.2,-40.7 42.4,-42.4 40.7,-27.2 55.4,-23 48.1,-9.6"/>
      <g transform="rotate(-15)" fill="var(--navy)" font-family="Roboto, Arial, sans-serif" font-weight="900" text-anchor="middle">
        <text x="-4" y="-4" font-size="30">$50</text>
        <text x="6" y="26" font-size="30">off</text>
      </g>
    </g>
  </svg>

  <div class="abs pill" style="left:25px;top:25px;width:141px;">REFER a Friend</div>
  <p class="abs code-label" style="left:206px;top:28px;">Promo<br>Code</p>
  <div class="abs code-box" style="left:256px;top:25px;width:100px;">REFER</div>
  <p class="abs body-copy" style="top:74px;">GIVE $100, GET $100<br>Give your friends $100 off their first purchase (over $500)<br>and receive a $100 discount on any order (over $500).</p>

  <div class="abs pill" style="left:25px;top:138px;width:141px;">1st Purchase</div>
  <p class="abs code-label" style="left:206px;top:141px;">Promo<br>Code</p>
  <div class="abs code-box" style="left:256px;top:138px;width:124px;">FIRST150</div>
  <p class="abs body-copy" style="top:188px;">$150 off your first department purchase of $500.</p>

  <p class="abs notice">PROMOTIONS CANNOT BE COMBINED</p>
  <p class="abs section-label" style="top:271px;">Refer Information</p>
  <p class="abs section-label" style="top:379px;">1st Purchase Information</p>

  <div class="abs stamp" role="img" aria-label="Postage stamp area"></div>
  <p class="abs return-copy">Lorem ipsum dolor sit amet, consectetuer adipiscing<br>Lorem ipsum dolor sit amet, consectetuer</p>
</section>

</body>
</html>
```